Create a professional, fresh and polished oversized post card for law firm specializing in Estate Planning & Probate Law for High Net Worth Clients

Use any picture(s) of your choice (mine or ones you recommend), logo, headshot and company info

www.morvenashcroftlaw.com

Westgate Office - 4100 Birchmont Road, Suite 1500, Charlotte, NC 28214
Kerrington Office - 13480 Oakridge Lane, Suite 300, Charlotte, NC 28269

Phone (704) 555-0187

Use this card for a Free Consultation

Target Market(s)

young and old families too; business owners

Industry/Entity Type

Law Firm

Font styles to use
Serif
Sans Serif

Requirements
Must have
• Use any picture(s) of your choice (mine or ones you recommend), logo, headshot and company info
• www.morvenashcroftlaw.com
• Westgate Office - 4100 Birchmont Road, Suite 1500, Charlotte, NC 28214
• Kerrington Office - 13480 Oakridge Lane, Suite 300, Charlotte, NC 28269
• Phone (704) 555-0187
• Use this card for a Free Consultation
Nice to have
• great colors and great design; like graphics with depth /shading
Should not have
• don't use too many pics - keep it simple

```html
<!DOCTYPE html>
<html lang="en">
<head>
<meta charset="utf-8">
<title>Morven Ashcroft Law – Postcard</title>
<link rel="stylesheet" href="https://fonts.googleapis.com/css2?family=Cinzel:wght@400;700&family=Lato:wght@400;700&family=Roboto+Condensed:wght@700&display=swap">
<style>
  :root {
    --brand-blue: #1a77a3;
    --brand-blue-deep: #14668e;
    --band-gray: #676767;
    --ink: #1b1b1b;
    --paper: #ffffff;
    --stamp-gray: #808080;
    --photo-sky-a: #b9d7ee;
    --photo-sky-b: #e8c7a5;
  }
  * { box-sizing: border-box; margin: 0; padding: 0; }
  html, body { width: 1200px; height: 1200px; overflow: hidden; background: var(--paper); }
  body { position: relative; font-family: "Lato", sans-serif; color: var(--ink); }

  .postcard {
    position: absolute; left: 196px; width: 804px; height: 520px;
    background: var(--paper); overflow: hidden;
    box-shadow: 4px 6px 10px rgba(0,0,0,.28);
  }
  .postcard--front { top: 60px; }
  .postcard--back { top: 618px; }
  .postcard__layer { position: absolute; inset: 0; width: 804px; height: 520px; }

  .photo { position: absolute; }
  .photo--round { border-radius: 50%; border: 5px solid var(--brand-blue); box-shadow: 0 0 0 3px var(--paper); }
  .photo--family-warm { background: radial-gradient(circle at 30% 35%, #f6e2c8, #d9a274 45%, #7d9cbd 80%, #5f86ad); }
  .photo--family-sky { background: linear-gradient(160deg, var(--photo-sky-a), var(--photo-sky-b) 60%, #c48c63); }
  .photo--headshot { background: radial-gradient(circle at 50% 40%, #ecd3a6, #c29b6c 45%, #e7a5b4 70%, #2a2a2a 85%); }
  .photo--child { background: radial-gradient(ellipse at 45% 50%, rgba(130,95,70,.30), rgba(255,255,255,0) 70%); }

  .brand { position: absolute; text-align: center; color: var(--paper); font-family: "Cinzel", serif; }
  .brand__dot { display: block; margin: 0 auto; border-radius: 50%; border: 2px solid currentColor; }
  .brand__name { display: block; font-weight: 400; letter-spacing: .04em; white-space: nowrap; }
  .brand__tag { display: flex; align-items: center; justify-content: center; gap: 6px; font-size: 7px; letter-spacing: .15em; }
  .brand__tag::before, .brand__tag::after { content: ""; height: 1px; background: currentColor; flex: 1; }

  .brand--front { left: 530px; top: 8px; width: 180px; }
  .brand--front .brand__dot { width: 60px; height: 60px; }
  .brand--front .brand__name { font-size: 19px; margin-top: 12px; border-top: 1px solid rgba(255,255,255,.6); padding-top: 1px; }
  .brand--back { left: 232px; top: 430px; width: 120px; }
  .brand--back .brand__dot { width: 40px; height: 40px; }
  .brand--back .brand__name { font-size: 12.5px; margin-top: 10px; border-top: 1px solid rgba(255,255,255,.6); }

  .headline { position: absolute; left: 14px; top: 106px; width: 300px; font-family: "Cinzel", serif; color: var(--ink); }
  .headline__lead { display: block; font-size: 24.5px; font-weight: 700; line-height: 1; white-space: nowrap; }
  .headline__sub { display: block; font-size: 13.6px; font-weight: 700; line-height: 1.25; white-space: nowrap; }
  .headline__key { display: block; font-size: 34.5px; font-weight: 700; color: var(--brand-blue); line-height: 1.1; white-space: nowrap; }

  .intro { position: absolute; left: 12px; top: 204px; width: 298px; font-size: 11.2px; line-height: 14px; text-align: justify; }

  .offer { position: absolute; left: 14px; top: 344px; width: 296px; padding: 5px 0; border-top: 1px solid var(--brand-blue); border-bottom: 1px solid var(--brand-blue); font-family: "Cinzel", serif; font-weight: 700; font-size: 12.4px; color: var(--brand-blue); text-align: center; white-space: nowrap; }

  .call { position: absolute; left: 14px; top: 382px; font-family: "Roboto Condensed", sans-serif; font-weight: 700; font-size: 28px; white-space: nowrap; }
  .call__label { color: var(--brand-blue); margin-right: 6px; }

  .site-line { position: absolute; left: 24px; top: 486px; color: var(--paper); font-size: 11.5px; letter-spacing: .36em; }

  .section-title { position: absolute; left: 14px; font-family: "Cinzel", serif; color: var(--brand-blue); font-size: 12.5px; line-height: 14px; }
  .section-title--main { top: 17px; }
  .section-title--list { top: 184px; width: 300px; }
  .estate-copy { position: absolute; left: 16px; top: 43px; width: 352px; font-size: 11.2px; line-height: 14px; text-align: justify; }

  .service-list { position: absolute; left: 18px; top: 220px; list-style: none; font-size: 11.2px; line-height: 16.8px; }
  .service-list li::before { content: ""; display: inline-block; width: 5px; height: 5px; border-radius: 50%; background: var(--brand-blue); margin-right: 7px; vertical-align: middle; }

  .offices { position: absolute; left: 22px; top: 403px; width: 232px; color: #e8e8e8; font-size: 9.2px; line-height: 12.4px; }
  .offices p + p { margin-top: 1px; }
  .offices__name { color: #2a8fc4; font-weight: 700; }
  .contact { position: absolute; left: 22px; top: 468px; color: #e8e8e8; font-size: 9.2px; line-height: 14px; }
  .contact__icon { display: inline-block; width: 9px; height: 7px; vertical-align: -1px; margin-right: 3px; }

  .stamp-box { position: absolute; left: 714px; top: 13px; width: 76px; height: 91px; background: var(--stamp-gray); }
</style>
</head>
<body>

<!-- FRONT -->
<section class="postcard postcard--front" aria-label="Postcard front">
  <svg class="postcard__layer" viewBox="0 0 804 520" aria-hidden="true">
    <rect width="804" height="520" fill="var(--brand-blue)"/>
  </svg>

  <svg class="postcard__layer" viewBox="0 0 804 520" role="img" aria-label="Photo of a smiling senior couple embracing in front of autumn foliage">
    <defs>
      <radialGradient id="autumnGlow" cx=".25" cy=".2" r=".8">
        <stop offset="0" stop-color="#f4c064"/>
        <stop offset=".45" stop-color="#d98a3e"/>
        <stop offset="1" stop-color="#b5652c"/>
      </radialGradient>
      <radialGradient id="shirtTone" cx=".8" cy=".8" r=".55">
        <stop offset="0" stop-color="#9eb2cc" stop-opacity=".95"/>
        <stop offset="1" stop-color="#9eb2cc" stop-opacity="0"/>
      </radialGradient>
      <radialGradient id="skinTone" cx=".55" cy=".4" r=".3">
        <stop offset="0" stop-color="#f1d2bd" stop-opacity=".8"/>
        <stop offset="1" stop-color="#f1d2bd" stop-opacity="0"/>
      </radialGradient>
    </defs>
    <path d="M420 150 C560 150 700 125 804 92 L804 520 L470 520 C420 420 400 300 420 150 Z" fill="url(#autumnGlow)"/>
    <path d="M420 150 C560 150 700 125 804 92 L804 520 L470 520 C420 420 400 300 420 150 Z" fill="url(#shirtTone)"/>
    <path d="M420 150 C560 150 700 125 804 92 L804 520 L470 520 C420 420 400 300 420 150 Z" fill="url(#skinTone)"/>
  </svg>

  <svg class="postcard__layer" viewBox="0 0 804 520" aria-hidden="true">
    <path d="M430 158 C570 160 700 132 804 100" fill="none" stroke="var(--band-gray)" stroke-width="20"/>
    <path d="M430 172 C570 174 700 146 804 114" fill="none" stroke="var(--paper)" stroke-width="3"/>
    <path d="M0 78 C130 45 300 40 440 108 C395 210 390 380 465 520 L0 520 Z" fill="var(--paper)"/>
    <path d="M0 68 C130 35 300 30 450 102" fill="none" stroke="var(--band-gray)" stroke-width="8"/>
    <path d="M445 110 C400 210 395 380 472 520" fill="none" stroke="var(--brand-blue)" stroke-width="7"/>
    <path d="M0 448 C150 470 300 478 425 440 C435 470 445 495 460 520 L0 520 Z" fill="var(--ink)"/>
    <path d="M0 438 C150 460 300 468 430 428" fill="none" stroke="var(--brand-blue)" stroke-width="4"/>
  </svg>

  <div class="brand brand--front">
    <span class="brand__dot"></span>
    <span class="brand__name">MORVEN ASHCROFT</span>
    <span class="brand__tag">LAW PLLC</span>
  </div>

  <div class="photo photo--round photo--family-warm" style="left:329px;top:77px;width:166px;height:166px;" role="img" aria-label="Photo of a smiling multi-generation family outdoors"></div>
  <div class="photo photo--child" style="left:318px;top:304px;width:110px;height:200px;" role="img" aria-label="Photo of a small child in an aviator cap holding a toy plane"></div>

  <h1 class="headline">
    <span class="headline__lead">SERVING CLIENTS WITH</span>
    <span class="headline__sub">COMPASSION AND LEGAL GUIDANCE</span>
    <span class="headline__key">IS OUR PASSION</span>
  </h1>

  <p class="intro">The Charlotte law firm of Morven Ashcroft Law, PLLC focuses on serving clients in the areas of: estate planning, estate administration, probate law, special needs planning, succession planning and general business law. Morven Ashcroft Law, PLLC is conveniently located in the Westgate Plaza in Charlotte, NC. Managing attorney Morven Ashcroft is a Board Certified Specialist in Estate Planning and Probate Law, Top Rated North Carolina Trusts and Estates Attorney, and a Peer Review Preeminent attorney by Lawrey-Benton.</p>

  <p class="offer">Use this card for a Free Consultation</p>

  <p class="call"><span class="call__label">CALL :</span>(704) 555-0187</p>
  <p class="site-line">www.morvenashcroftlaw.com</p>
</section>

<!-- BACK -->
<section class="postcard postcard--back" aria-label="Postcard back">
  <svg class="postcard__layer" viewBox="0 0 804 520" aria-hidden="true">
    <path d="M0 358 C110 352 200 338 280 314 L420 320 C412 420 408 470 406 520 L0 520 Z" fill="var(--ink)"/>
    <path d="M0 344 C110 338 200 324 285 298" fill="none" stroke="var(--band-gray)" stroke-width="0"/>
    <path d="M0 344 C110 338 200 324 285 298" fill="none" stroke="var(--brand-blue)" stroke-width="9"/>
    <path d="M342 0 C372 50 394 120 402 190" fill="none" stroke="var(--band-gray)" stroke-width="9"/>
    <path d="M360 0 C398 70 418 150 416 240 C414 330 408 430 406 520" fill="none" stroke="var(--brand-blue)" stroke-width="9"/>
  </svg>

  <div class="stamp-box" aria-hidden="true"></div>

  <h2 class="section-title section-title--main">ESTATE PLANNING</h2>
  <p class="estate-copy">A carefully planned estate is very important to ensure that your assets transfer according to your wishes. Without a Will, your probate assets pass according to state law, which may likely result in assets not passing according to your wishes. Dying without a Will often results in conflicts among heirs as well as unnecessary delays and expenses. A properly planned estate directs the distribution of your assets, contemplates estate and income tax planning, and eliminates uncertainties and potential estate disputes.</p>

  <h2 class="section-title section-title--list">ESTATE PLANNING IS A COMPREHENSIVE PROCESS WHICH MAY INCLUDE:</h2>
  <ul class="service-list">
    <li>Last Will and Testament</li>
    <li>Revocable Trusts and Irrevocable Trusts</li>
    <li>Powers of Attorney</li>
    <li>Health Care Powers of Attorney and Living Wills</li>
    <li>Life Insurance</li>
    <li>Succession Planning</li>
  </ul>

  <div class="photo photo--round photo--family-sky" style="left:300px;top:140px;width:140px;height:140px;" role="img" aria-label="Photo of a young family smiling together under a blue sky"></div>
  <div class="photo photo--round photo--headshot" style="left:264px;top:270px;width:160px;height:160px;" role="img" aria-label="Headshot of the managing attorney"></div>

  <div class="offices">
    <p><span class="offices__name">Westgate Office</span> - 4100 Birchmont Road, Suite 1500, Charlotte, NC 28214</p>
    <p><span class="offices__name">Kerrington Office</span> - 13480 Oakridge Lane, Suite 300, Charlotte, NC 28269</p>
  </div>
  <div class="contact">
    <p><svg class="contact__icon" viewBox="0 0 9 7"><rect x=".5" y=".5" width="8" height="6" fill="none" stroke="#2a8fc4"/><path d="M.5 .5 L4.5 4 L8.5 .5" fill="none" stroke="#2a8fc4"/></svg>(704) 555-0187</p>
    <p><svg class="contact__icon" viewBox="0 0 9 7"><circle cx="4.5" cy="3.5" r="3" fill="none" stroke="#2a8fc4"/></svg>www.morvenashcroftlaw.com</p>
  </div>

  <div class="brand brand--back">
    <span class="brand__dot"></span>
    <span class="brand__name">MORVEN ASHCROFT</span>
    <span class="brand__tag">LAW PLLC</span>
  </div>
</section>

</body>
</html>
```